Business Card Design Project

we need a business card design for our company: www.plomvik.ch
It's important to include our already existing logo (see website)

```html
<!DOCTYPE html>
<html lang="de">
<head>
<meta charset="utf-8">
<title>Plomvik – Visitenkarte</title>
<link rel="stylesheet" href="https://fonts.googleapis.com/css2?family=Questrial&display=swap">
<style>
  :root {
    --stage: #3b3b3d;
    --card: #f4f5f7;
    --card-shade: #e3e6ea;
    --brand-light: #6fa3dc;
    --brand-dark: #1670c2;
    --label: #8a96a6;
  }
  * { margin: 0; padding: 0; box-sizing: border-box; }
  html, body { width: 1200px; height: 534px; overflow: hidden; }
  body {
    background: var(--stage);
    font-family: "Questrial", "Century Gothic", sans-serif;
    position: relative;
  }
  .card {
    position: absolute;
    top: 124px;
    width: 502px;
    height: 286px;
    border-radius: 16px;
    overflow: hidden;
    background: var(--card);
  }
  .card--front { left: 78px; }
  .card--back { left: 622px; }
  .card__texture {
    position: absolute;
    inset: 0;
    background:
      radial-gradient(ellipse at 75% 35%, var(--card-shade) 0%, rgba(227,230,234,0) 60%),
      linear-gradient(135deg, #f7f8fa 0%, #eceef1 55%, #f5f6f8 100%);
  }
  .wordmark {
    position: absolute;
    color: var(--brand-light);
    font-weight: 400;
    line-height: 1;
    letter-spacing: 0.5px;
  }
  .card--front .wordmark { left: 46px; top: 35px; font-size: 46px; }
  .card--back .wordmark { left: 0; right: 0; top: 104px; text-align: center; font-size: 84px; }
  .company {
    position: absolute;
    left: 56px;
    top: 130px;
    color: var(--brand-dark);
    font-size: 20px;
  }
  .address {
    position: absolute;
    left: 56px;
    top: 160px;
    color: var(--brand-dark);
    font-size: 13.5px;
    line-height: 16px;
    font-style: normal;
  }
  .contacts {
    position: absolute;
    left: 56px;
    top: 199px;
    list-style: none;
    font-size: 12.5px;
    line-height: 12.5px;
  }
  .contacts__label { color: var(--label); font-size: 9px; }
  .contacts__sep { color: var(--label); font-size: 9px; margin: 0 3px; }
  .contacts__value { color: var(--brand-dark); }
  .website {
    position: absolute;
    left: 0;
    right: 0;
    top: 213px;
    text-align: center;
    color: var(--brand-dark);
    font-size: 18px;
    letter-spacing: 0.3px;
  }
</style>
</head>
<body>
  <section class="card card--front">
    <div class="card__texture" role="img" aria-label="Soft light-grey background with faint overlapping embossed squares"></div>
    <div class="wordmark">Plomvik</div>
    <h1 class="company" style="font-weight:400">Plomvik AG</h1>
    <address class="address">Mühlenrain 14<br>8052 Zürich</address>
    <ul class="contacts">
      <li><span class="contacts__label">Telephone</span><span class="contacts__sep">|</span><span class="contacts__value">+41 44 000 12 34</span></li>
      <li><span class="contacts__label">Email</span><span class="contacts__sep">|</span><span class="contacts__value">info@plomvik.ch</span></li>
      <li><span class="contacts__label">Skype</span><span class="contacts__sep">|</span><span class="contacts__value">plomvik.ch</span></li>
      <li><span class="contacts__label">Website</span><span class="contacts__sep">|</span><span class="contacts__value">www.plomvik.ch</span></li>
    </ul>
  </section>

  <section class="card card--back">
    <div class="card__texture" role="img" aria-label="Soft light-grey background with faint overlapping embossed squares"></div>
    <div class="wordmark">Plomvik</div>
    <div class="website">www.plomvik.ch</div>
  </section>
</body>
</html>
```